High end wine label at Austrian Winery

We are a traditional winery in Austria in region Burgenland. We are looking for a relaunch of our current wine label for our [vantor] series. It's a high end wine series at an upper price range. At the moment we have just two kinds of the label, one white one for the white wines and one black one for the red wines. This is a series of wine, white, red, sweet, sparkling and a top wine categories. So we need the same label, but in 4 different ways to distinguish the wines plus the sparkling. Maybe in color, patterns, ... or something else. The label should be very simple, including our new logo. It's also possible to make one label but we can splitting two parts of the label. The size of the label does not matter, need not be the same as now. It's a bit higher than a normal bottle. Additionally we need a back label with wine description and the wine dates on it.

Target Market(s)

private consumers and restaurants, no retailers

Colors

Designer to choose colors to be used in the design.

Requirements
Must have
• simple label with 4 different categories (red, white, sweet, top) plus Frizzante label, new logo integrated, high end label. Just logo, grape variety and [vantor] as text on the front label as text
Nice to have
• It's just good, if there'sa possibility to have different colors of each grape variety (about 10 different), but all the same style. top Wines should have an extraordinary design, but familiar with the others
Should not have
• no cheap look

```html
<!DOCTYPE html>
<html lang="en">
<head>
<meta charset="utf-8">
<title>Wine Label Series – Concept</title>
<link rel="stylesheet" href="https://fonts.googleapis.com/css2?family=EB+Garamond:wght@400;500&family=Montserrat:wght@400;700&display=swap">
<style>
  :root {
    --bg: #ffffff;
    --gold-light: #e8cf63;
    --gold: #c9a733;
    --gold-dark: #a9871f;
    --charcoal: #3b3b3b;
    --silver-light: #c9c9c9;
    --silver-dark: #8e8e8e;
    --wine-red: #6b1a1f;
    --ink-dark: #1d1d1d;
    --ink-light: #ffffff;
    --message: #8b1f1f;
    --amber: #d6a21b;
    --olive: #8a7a1c;
  }
  * { margin: 0; padding: 0; box-sizing: border-box; }
  html, body { width: 1154px; height: 1200px; overflow: hidden; background: var(--bg); }
  .canvas { position: relative; width: 1154px; height: 1200px; background: var(--bg); }

  .label { position: absolute; }
  .label svg { display: block; }

  .sparkling-label {
    left: 169px; top: 525px; width: 144px; height: 177px;
    background: linear-gradient(160deg, var(--gold-light) 0%, var(--gold) 55%, var(--gold-dark) 100%);
    text-align: center; color: var(--ink-dark);
  }
  .sparkling-label .pattern-strip {
    height: 15px;
    background: linear-gradient(90deg, #e9dfb0, #f4eed2, #d9cc8f, #f1e9c6);
  }
  .sparkling-label .variety {
    font-family: "EB Garamond", serif; font-size: 13px; letter-spacing: 0.3px; margin-top: 12px;
  }
  .sparkling-label .style {
    font-family: "Montserrat", sans-serif; font-size: 7.5px; margin-top: 3px; letter-spacing: 0.3px;
  }
  .sparkling-label .brand-mark {
    width: 60px; height: 60px; border-radius: 50%; border: 2px solid var(--ink-dark);
    margin: 14px auto 0;
  }
  .sparkling-label .brand-name {
    font-family: "EB Garamond", serif; font-size: 14px; letter-spacing: 2px; margin-top: 4px;
  }

  .ribbon-label { top: 395px; width: 94px; height: 277px; }
  .ribbon-label.traminer { left: 519px; }
  .ribbon-label.pinot-blanc { left: 733px; }
  .ribbon-label.cuvee { left: 959px; }

  .variety-text { font-family: "EB Garamond", serif; font-size: 11px; }
  .series-text { font-family: "Montserrat", sans-serif; font-size: 5.5px; }
  .brand-text { font-family: "EB Garamond", serif; font-size: 13px; letter-spacing: 2px; }

  .message {
    position: absolute; left: 139px; top: 1018px;
    font-family: "EB Garamond", serif; font-size: 30px; line-height: 35.5px;
    color: var(--message); text-transform: uppercase; letter-spacing: -0.2px;
  }
</style>
</head>
<body>
<main class="canvas">

  <section class="label sparkling-label">
    <div class="pattern-strip" role="img" aria-label="Decorative sparkling bubble pattern band"></div>
    <p class="variety">FRIZZANTE</p>
    <p class="style">SCHAUMWEIN</p>
    <div class="brand-mark"></div>
    <p class="brand-name">HALDEN</p>
  </section>

  <section class="label ribbon-label traminer">
    <svg width="94" height="277" viewBox="0 0 94 277">
      <polygon points="0,0 94,0 94,277 0,218" fill="var(--charcoal)"/>
      <rect x="0" y="0" width="94" height="16" fill="#ece6d6" role="img" aria-label="Decorative light ornamental pattern band"/>
      <text class="variety-text" x="47" y="43" text-anchor="middle" fill="var(--ink-light)">TRAMINER</text>
      <text class="series-text" x="47" y="55" text-anchor="middle" fill="var(--ink-light)">[VANTOR]</text>
      <path d="M94,122 C84,118 72,108 68,96" fill="none" stroke="var(--amber)" stroke-width="4"/>
      <polygon points="60,100 68,86 75,99" fill="var(--amber)"/>
      <circle cx="47" cy="163" r="30" fill="none" stroke="var(--ink-light)" stroke-width="2"/>
      <text class="brand-text" x="47" y="210" text-anchor="middle" fill="var(--ink-light)">HALDEN</text>
    </svg>
  </section>

  <section class="label ribbon-label pinot-blanc">
    <svg width="94" height="277" viewBox="0 0 94 277">
      <defs>
        <linearGradient id="silverFill" x1="0" y1="0" x2="1" y2="1">
          <stop offset="0" stop-color="var(--silver-light)"/>
          <stop offset="1" stop-color="var(--silver-dark)"/>
        </linearGradient>
      </defs>
      <polygon points="0,0 94,0 94,277 0,218" fill="url(#silverFill)"/>
      <rect x="0" y="0" width="94" height="16" fill="#4a4232" role="img" aria-label="Decorative dark ornamental pattern band"/>
      <text class="variety-text" x="47" y="43" text-anchor="middle" fill="var(--ink-light)">PINOT BLANC</text>
      <text class="series-text" x="47" y="55" text-anchor="middle" fill="var(--ink-light)">[VANTOR]</text>
      <path d="M94,122 C84,118 72,108 68,96" fill="none" stroke="var(--olive)" stroke-width="4"/>
      <polygon points="60,100 68,86 75,99" fill="var(--olive)"/>
      <circle cx="47" cy="163" r="30" fill="none" stroke="var(--ink-light)" stroke-width="2"/>
      <text class="brand-text" x="47" y="210" text-anchor="middle" fill="var(--ink-light)">HALDEN</text>
    </svg>
  </section>

  <section class="label ribbon-label cuvee">
    <svg width="94" height="277" viewBox="0 0 94 277">
      <defs>
        <linearGradient id="goldFill" x1="0" y1="0" x2="1" y2="1">
          <stop offset="0" stop-color="var(--gold-light)"/>
          <stop offset="0.55" stop-color="var(--gold)"/>
          <stop offset="1" stop-color="var(--gold-dark)"/>
        </linearGradient>
      </defs>
      <polygon points="0,0 94,0 94,277 0,218" fill="url(#goldFill)"/>
      <rect x="0" y="0" width="94" height="16" fill="#8c2a1e" role="img" aria-label="Decorative red ornamental pattern band"/>
      <text class="variety-text" x="47" y="43" text-anchor="middle" fill="var(--ink-dark)">SELEGD CUVEE</text>
      <text class="series-text" x="47" y="55" text-anchor="middle" fill="var(--ink-dark)">[VANTOR]</text>
      <path d="M94,122 C84,118 72,108 68,96" fill="none" stroke="var(--wine-red)" stroke-width="4"/>
      <polygon points="60,100 68,86 75,99" fill="var(--wine-red)"/>
      <circle cx="47" cy="163" r="30" fill="none" stroke="var(--ink-dark)" stroke-width="2"/>
      <text class="brand-text" x="47" y="210" text-anchor="middle" fill="var(--ink-dark)">HALDEN</text>
    </svg>
  </section>

  <p class="message">
    Dear customer, this is just&nbsp; an example of what<br>
    we can create together. If you like please coment<br>
    to take it to next level, if not, please do nothing<br>
    and im ok with that.<br>
    Thank you
  </p>

</main>
</body>
</html>
```